Trade Show Booth for SaaS Company

Brightwave Mailer is a startup company that will be exhibiting its software as a service product at a trade show in the near future. We are looking for something that really pops and is appealing to the eye. Attached is the branding guidelines along with the color palette.
Also attached is a previous design we have used and you can take to logo and designs elements for the updated design. This trade show targets a different customer and the design and copy needs to change. We no longer want the "hub and spoke" graphic in the middle.
Here's the copy...
Headline:
Super Charge Your Email Marketing
Main Copy:
What can email do for you?
• Maximize ROI
• Strengthen relationships
• Drive engagement
• Increase conversions
We handle email—so you can focus on growth.
From a design standpoint I would recommend:
1. Email Iconography:
Use glowing, stylized email icons next to each bullet point to visually break up the text and add a modern, engaging element.
2. Badge for Experience:
Create a prominent badge or ribbon highlighting “Over 20 years of experience,” placed in the bottom corner to emphasize expertise.
3. ROI Graphic:
Incorporate a subtle upward-trending arrow or graph behind the “Maximize ROI” bullet point to visually reinforce the concept of growth and success.
I would like to see a email icon and a lighting bolt somehow incorporated into the main headline of the back drop .
Lastly, the printing specs are attached.
Target Market(s)
Business Owners

```html
<!DOCTYPE html>
<html lang="en">
<head>
<meta charset="utf-8">
<title>Brightwave Mailer – Trade Show Backdrop</title>
<link href="https://fonts.googleapis.com/css2?family=Bebas+Neue&family=Fredoka:wght@500&family=Montserrat:wght@700&display=swap" rel="stylesheet">
<style>
  :root {
    --stage: #a3a3a3;
    --white: #ffffff;
    --magenta: #ec1e7f;
    --blush: #f8d5e5;
    --rose: #f09cc3;
    --ink: #1d1a2b;
    --badge: #e55a9f;
  }
  * { margin: 0; padding: 0; box-sizing: border-box; }
  html, body {
    width: 857px;
    height: 1200px;
    overflow: hidden;
    background: var(--stage);
  }
  .canvas {
    width: 857px;
    height: 1200px;
    display: flex;
    align-items: center;
    justify-content: center;
  }
  .backdrop {
    width: 817px;
    height: 512px;
    display: block;
    box-shadow: 0 10px 24px rgba(0,0,0,0.35);
  }
  .headline {
    font-family: "Bebas Neue", Impact, sans-serif;
    font-size: 66px;
    fill: var(--ink);
  }
  .brand-name {
    font-family: "Bebas Neue", Impact, sans-serif;
    font-size: 72px;
    fill: var(--ink);
  }
  .benefit {
    font-family: "Fredoka", Arial, sans-serif;
    font-weight: 500;
    font-size: 23px;
    fill: var(--white);
  }
  .tagline {
    font-family: "Bebas Neue", Impact, sans-serif;
    font-size: 40px;
    fill: var(--white);
  }
  .web-address {
    font-family: "Montserrat", Arial, sans-serif;
    font-weight: 700;
    font-size: 21px;
    fill: var(--magenta);
  }
  .badge-text {
    font-family: "Bebas Neue", Impact, sans-serif;
    fill: var(--white);
  }
  .benefit-icon .ring { fill: none; stroke: var(--white); stroke-width: 2.5; }
  .benefit-icon .glyph { fill: var(--white); }
  .benefit-icon .glyph-line { fill: none; stroke: var(--white); stroke-width: 2.5; stroke-linecap: round; stroke-linejoin: round; }
</style>
</head>
<body>
<main class="canvas">
  <svg class="backdrop" viewBox="0 0 1230 770" xmlns="http://www.w3.org/2000/svg" role="img" aria-label="Brightwave Mailer trade show backdrop: Super Charge Your Email Marketing">
    <rect class="backdrop-base" x="0" y="0" width="1230" height="770" fill="var(--white)"/>
    <rect class="lower-field" x="0" y="500" width="1230" height="270" fill="var(--magenta)"/>

    <polygon class="bolt-accent" points="665,0 725,0 650,225 705,225 725,405 675,405 660,275 555,275" fill="var(--blush)"/>

    <rect class="headline-band" x="145" y="405" width="940" height="96" fill="var(--blush)"/>
    <text class="headline" x="615" y="478" text-anchor="middle" textLength="830" lengthAdjust="spacingAndGlyphs">SUPER CHARGE YOUR EMAIL MARKETING</text>

    <path class="side-curve" d="M0,0 L40,0 Q250,385 20,770 L0,770 Z" fill="var(--white)"/>
    <path class="side-arc" d="M0,10 Q150,385 0,760 L0,770 L20,770 Q120,385 0,0 Z" fill="var(--rose)"/>
    <path class="side-arc-inner" d="M20,0 Q175,385 20,770" fill="none" stroke="var(--rose)" stroke-width="14"/>
    <text class="web-address" transform="translate(82 385) rotate(-90)" text-anchor="middle" textLength="320" lengthAdjust="spacingAndGlyphs">www.mailerhubly.com</text>

    <path class="side-curve" d="M1230,0 L1190,0 Q980,385 1210,770 L1230,770 Z" fill="var(--white)"/>
    <path class="side-arc" d="M1230,10 Q1080,385 1230,760 L1230,770 L1210,770 Q1110,385 1230,0 Z" fill="var(--rose)"/>
    <path class="side-arc-inner" d="M1210,0 Q1055,385 1210,770" fill="none" stroke="var(--rose)" stroke-width="14"/>
    <text class="web-address" transform="translate(1162 385) rotate(-90)" text-anchor="middle" textLength="320" lengthAdjust="spacingAndGlyphs">www.mailerhubly.com</text>

    <g class="brand-lockup">
      <rect class="brand-square" x="200" y="288" width="46" height="46" fill="var(--magenta)"/>
      <text class="brand-name" x="262" y="336">BRIGHTWAVE MAILER</text>
    </g>

    <g class="benefit-icon" transform="translate(230 538)">
      <circle class="ring" r="21"/>
      <rect class="glyph" x="-9" y="2" width="4" height="8"/>
      <rect class="glyph" x="-3" y="-3" width="4" height="13"/>
      <rect class="glyph" x="3" y="-8" width="4" height="18"/>
      <polyline class="glyph-line" points="-11,-4 -3,-11 9,-14"/>
    </g>
    <text class="benefit" x="263" y="546">Maximize ROI</text>

    <g class="benefit-icon" transform="translate(520 536)">
      <circle class="ring" r="21"/>
      <circle class="glyph" cx="0" cy="-7" r="4"/>
      <circle class="glyph" cx="-9" cy="6" r="4"/>
      <circle class="glyph" cx="9" cy="6" r="4"/>
      <polyline class="glyph-line" points="-6,3 0,-3 6,3"/>
    </g>
    <text class="benefit" x="555" y="544">Strengthen relationships</text>

    <g class="benefit-icon" transform="translate(230 598)">
      <circle class="ring" r="21"/>
      <rect class="glyph-line" x="-11" y="-8" width="22" height="15" rx="2"/>
      <polyline class="glyph-line" points="-11,-8 0,1 11,-8"/>
    </g>
    <text class="benefit" x="263" y="606">Drive engagement</text>

    <g class="benefit-icon" transform="translate(520 600)">
      <circle class="ring" r="21"/>
      <rect class="glyph" x="-9" y="2" width="4" height="8"/>
      <rect class="glyph" x="-3" y="-2" width="4" height="12"/>
      <polyline class="glyph-line" points="5,10 5,-10"/>
      <polyline class="glyph-line" points="1,-6 5,-11 9,-6"/>
    </g>
    <text class="benefit" x="555" y="608">Increase conversions</text>

    <text class="tagline" x="205" y="684" textLength="640" lengthAdjust="spacingAndGlyphs">WE HANDLE EMAIL—SO YOU CAN FOCUS ON GROWTH.</text>

    <g class="experience-badge" transform="translate(950 605)">
      <circle r="97" fill="var(--white)"/>
      <g fill="var(--white)">
        <circle cx="0" cy="-92" r="14"/><circle cx="46" cy="-80" r="14"/><circle cx="80" cy="-46" r="14"/>
        <circle cx="92" cy="0" r="14"/><circle cx="80" cy="46" r="14"/><circle cx="46" cy="80" r="14"/>
        <circle cx="0" cy="92" r="14"/><circle cx="-46" cy="80" r="14"/><circle cx="-80" cy="46" r="14"/>
        <circle cx="-92" cy="0" r="14"/><circle cx="-80" cy="-46" r="14"/><circle cx="-46" cy="-80" r="14"/>
      </g>
      <circle r="80" fill="var(--badge)"/>
      <text class="badge-text" y="-22" text-anchor="middle" font-size="36">OVER</text>
      <text class="badge-text" y="22" text-anchor="middle" font-size="50">20 YEARS</text>
      <text class="badge-text" y="48" text-anchor="middle" font-size="21">OF EXPERIENCE</text>
    </g>
  </svg>
</main>
</body>
</html>
```